Business Card Design

Harbourline Recruitment is a specialist financial services recruitment company and implementation partner

Industry/Entity Type

Business

Contact Information for Business Card

Tom Vale
Harbourline Recruiment Ltd
e:tom.vale@harbourline-recruitment.example
m:07834 262 418
m:07722 584 301
s: tommvale

```html
<!DOCTYPE html>
<html lang="en">
<head>
<meta charset="utf-8">
<title>Harbourline Recruitment – Business Card</title>
<link rel="stylesheet" href="https://fonts.googleapis.com/css2?family=Questrial&family=Arimo:wght@400;700&display=swap">
<style>
  :root {
    --page-bg: #e8e5e1;
    --card-black: #000000;
    --card-white: #ffffff;
    --ink: #1a1a1a;
    --icon-grey: #7a7a7a;
    --skyline-light: #ffffff;
    --skyline-shade: #d8d8d8;
  }
  * { margin: 0; padding: 0; box-sizing: border-box; }
  html, body {
    width: 1200px; height: 533px; overflow: hidden;
    background: var(--page-bg);
  }
  .stage { position: relative; width: 1200px; height: 533px; }

  .card {
    position: absolute; top: 149px;
    width: 433px; height: 235px; overflow: hidden;
  }
  .card--front { left: 154px; background: var(--card-black); }
  .card--back  { left: 612px; background: var(--card-white); }

  .brand {
    position: absolute; left: 37px; top: 38px;
    color: var(--card-white);
    font-family: "Questrial", sans-serif; font-weight: 400;
  }
  .brand__name { font-size: 46px; line-height: 46px; letter-spacing: -0.5px; }
  .brand__sub  {
    font-size: 10px; line-height: 10px; letter-spacing: 0.2px;
    text-transform: uppercase; margin-top: 1px; padding-left: 2px;
    border-left: 1px solid var(--card-white);
  }

  .skyline {
    position: absolute; right: 0; bottom: 0;
    width: 210px; height: 166px;
  }

  .person {
    position: absolute; left: 0; right: 0; top: 104px;
    text-align: center; color: var(--ink);
  }
  .person__name {
    font-family: "Questrial", sans-serif;
    font-size: 27px; line-height: 27px; letter-spacing: 1px;
  }
  .person__role {
    font-family: "Arimo", sans-serif;
    font-size: 10px; line-height: 12px; margin-top: 1px;
  }

  .contacts {
    position: absolute; left: 108px; top: 181px;
    font-family: "Arimo", sans-serif; font-size: 9.5px; line-height: 12.5px;
    color: var(--ink);
  }
  .contacts__row { display: flex; align-items: center; white-space: nowrap; }
  .contacts__item { display: inline-flex; align-items: center; margin-right: 3px; }
  .contacts__item--bold { font-weight: 700; font-size: 10.5px; }
  .icon {
    width: 8px; height: 8px; margin-right: 4px; flex: none;
  }
</style>
</head>
<body>
<main class="stage">

  <section class="card card--front" aria-label="Card front">
    <div class="brand">
      <div class="brand__name">harbourline</div>
      <div class="brand__sub">Recruitment</div>
    </div>
    <svg class="skyline" role="img" aria-label="White silhouette of a city skyline with towers and an observation wheel" viewBox="0 0 210 166" preserveAspectRatio="none">
      <defs>
        <linearGradient id="skylineFade" x1="0" y1="0" x2="0" y2="1">
          <stop offset="0" stop-color="var(--skyline-shade)" stop-opacity="0.25"/>
          <stop offset="1" stop-color="var(--skyline-light)"/>
        </linearGradient>
      </defs>
      <rect width="210" height="166" fill="url(#skylineFade)"/>
    </svg>
  </section>

  <section class="card card--back" aria-label="Card back">
    <div class="person">
      <div class="person__name">tom vale</div>
      <div class="person__role">managing director</div>
    </div>

    <div class="contacts">
      <div class="contacts__row">
        <span class="contacts__item">
          <svg class="icon" viewBox="0 0 8 8" aria-hidden="true"><circle cx="4" cy="4" r="4" fill="var(--icon-grey)"/><path d="M2 2.8h4v2.6H2z M2 2.8l2 1.5 2-1.5" fill="none" stroke="#fff" stroke-width="0.6"/></svg>
          tom.vale@harbourline-recruitment.example
        </span>
      </div>
      <div class="contacts__row">
        <span class="contacts__item contacts__item--bold">
          <svg class="icon" viewBox="0 0 8 8" aria-hidden="true"><circle cx="4" cy="4" r="4" fill="var(--icon-grey)"/><rect x="2.9" y="1.8" width="2.2" height="4.4" rx="0.4" fill="none" stroke="#fff" stroke-width="0.6"/></svg>
          +44 7722 584 301
        </span>
        <span class="contacts__item contacts__item--bold">
          <svg class="icon" viewBox="0 0 8 8" aria-hidden="true"><circle cx="4" cy="4" r="4" fill="var(--icon-grey)"/><rect x="2.9" y="1.8" width="2.2" height="4.4" rx="0.4" fill="none" stroke="#fff" stroke-width="0.6"/></svg>
          +44 7834 262 418
        </span>
      </div>
      <div class="contacts__row">
        <span class="contacts__item">
          <svg class="icon" viewBox="0 0 8 8" aria-hidden="true"><circle cx="4" cy="4" r="4" fill="var(--icon-grey)"/></svg>
          tommvale
        </span>
        <span class="contacts__item">
          <svg class="icon" viewBox="0 0 8 8" aria-hidden="true"><circle cx="4" cy="4" r="4" fill="var(--icon-grey)"/><circle cx="4" cy="4" r="2.2" fill="none" stroke="#fff" stroke-width="0.6"/><path d="M1.8 4h4.4" stroke="#fff" stroke-width="0.6"/></svg>
          harbourline-recruitment.example
        </span>
      </div>
    </div>
  </section>

</main>
</body>
</html>
```